TrueGrindz Complete Stationery - Logo already designed

I already have the logo designed see attached. I need have a full set of stationary and business card designed for printing. I have attached an example of what I mean.

Please feel free to be creative. Also you can use the X in the logo by its self if you think it will work.

My details:

Name: Corwin Lestak
Social media handles: @corwinlestak
W: corwinlestak.com
E: info@corwinlestak.com
​P: 08 7493 5286
PO Box 7382, Westmere 6082
ABN 83 402 719 265

Target Market(s)

Anyone looking to be inspired.

Industry/Entity Type

Business

Font styles to use
Sans Serif

Colors
fbee3e
000000

Requirements
Must have
• My details:
• Name: Corwin Lestak
• Social media handles: @corwinlestak
• W: corwinlestak.com
• E: info@corwinlestak.com
• ​P: 08 7493 5286
• PO Box 7382, Westmere 6082
• ABN 83 402 719 265
Nice to have
• Something a little different
Should not have
• must not look tacky.

```html
<!DOCTYPE html>
<html lang="en">
<head>
<meta charset="utf-8">
<title>TrueGrindz Business Card</title>
<link href="https://fonts.googleapis.com/css2?family=Source+Sans+3:wght@400;700;900&display=swap" rel="stylesheet">
<style>
  :root {
    --ink: #231f20;
    --paper: #ffffff;
    --accent: #f9b92c;
    --backdrop: #d4d4d4;
    --rule: #9a9a9a;
    --muted: #bdbdbd;
  }
  * { margin: 0; padding: 0; box-sizing: border-box; }
  html, body {
    width: 1200px; height: 1200px; overflow: hidden;
    background: var(--backdrop);
    font-family: "Source Sans 3", sans-serif;
  }
  .sheet { position: relative; width: 1200px; height: 1200px; }
  .card {
    position: absolute; left: 180px; width: 840px; height: 480px;
    box-shadow: 0 10px 30px rgba(0,0,0,0.18);
    overflow: hidden;
  }
  .card--back { top: 70px; background: var(--ink); }
  .card--front { top: 630px; background: var(--paper); }

  .wordmark {
    position: absolute; font-weight: 900; letter-spacing: -1px;
    line-height: 1; white-space: nowrap;
  }
  .card--back .wordmark {
    color: var(--paper); font-size: 104px;
    left: 0; right: 0; text-align: center; top: 150px;
  }
  .card--back .handle {
    position: absolute; left: 0; right: 0; top: 300px;
    text-align: center; color: var(--muted);
    font-size: 22px; letter-spacing: 1px;
  }
  .card--front .wordmark {
    color: var(--ink); font-size: 92px; left: 330px; top: 52px;
  }
  .holder {
    position: absolute; left: 70px; top: 165px;
  }
  .holder__name {
    color: var(--accent); font-size: 34px; font-weight: 400; margin-bottom: 14px;
  }
  .holder__address { color: var(--ink); font-size: 22px; line-height: 1.3; }
  .divider {
    position: absolute; left: 400px; top: 210px; width: 1px; height: 140px;
    background: var(--rule);
  }
  .contacts {
    position: absolute; left: 430px; top: 205px;
    list-style: none; font-size: 23px; line-height: 1.42; color: var(--ink);
  }
  .contacts .label { color: var(--accent); }
  .band {
    position: absolute; left: 0; right: 0; bottom: 0; height: 52px;
    background: var(--ink);
  }
  .band-mark {
    position: absolute; left: 520px; bottom: 20px; width: 64px; height: 64px;
    background: var(--accent);
  }
</style>
</head>
<body>
<main class="sheet">
  <section class="card card--back" aria-label="Card back">
    <div class="wordmark">TrueGrindz</div>
    <div class="handle">@corwinlestak</div>
  </section>

  <section class="card card--front" aria-label="Card front">
    <div class="wordmark">TrueGrindz</div>
    <div class="holder">
      <p class="holder__name">Corwin Lestak</p>
      <p class="holder__address">PO Box 7382,<br>Westmere 6082</p>
    </div>
    <div class="divider"></div>
    <ul class="contacts">
      <li><span class="label">P:</span> 08 7493 5286</li>
      <li><span class="label">E:</span> info@corwinlestak.com</li>
      <li><span class="label">W:</span> corwinlestak.com</li>
      <li><span class="label">ABN:</span> 83 402 719 265</li>
    </ul>
    <div class="band"></div>
    <div class="band-mark"></div>
  </section>
</main>
</body>
</html>
```